Successful Software Co Launching A Super FUN Mobile & Web Application - ROCKSTAR Designer Needed

Our App is called "Sparkle Pennant"It is an employee "gamification" app designed to make working at your job fun...Employees complete simple tasks throughout the work day and are rewarded with points they can redeem for different gifts and benefits...We an AMAZING User Interface designed for both the mobile app and website app. We are looking for a clean, modern and simple design... This app is designed to make employees more engaged at work while having fun doing the things they already do each day...They can then redeem their points for rewards. It needs to be easy to understand and simple in its design...Example: A local carpet cleaning business uses our app.Their employees show up to work on time - They get 50 pointsThey clean out their work vehicle - They get 100 pointsThey up-sell an additional cleaning job - The get 250 pointsEtc...The app will also have fun icons and graphics that appear on the screen when an employee accomplishes a task.The app will play fun music sounds when they accomplish tasks too.
Updates

Need extra days to review

Target Market(s)

Small business owners

Logo Text

Sparkle Pennant

Font styles to use
Sans Serif

Colors

Designer to choose colors to be used in the design.

Requirements
Must have
• Simple elegant design
Nice to have
• I'd like to see examples of fun "icons" that could pop up on the screen after an employee completes a "task" and earns points... Something fun to pop up on the screen... (like a happy face, a thumbs up, fun text bubbles... "Way To Go!" etc... or any other fun ideas)

```html
<!DOCTYPE html>
<html lang="en">
<head>
<meta charset="utf-8">
<title>Sparkle Pennant – Home</title>
<link rel="stylesheet" href="https://fonts.googleapis.com/css2?family=Roboto:wght@300;400;500;700;900&family=Poppins:wght@700&display=swap">
<style>
  :root {
    --bg-start: #7a7cbc;
    --bg-end: #d3d3ea;
    --navy: #2b2d8f;
    --navy-deep: #2c2a7c;
    --brand-blue: #29a9e1;
    --orange: #f7941d;
    --muted: #a0a0a8;
    --text: #333340;
    --track: #e6e6f2;
    --screen: #fbfbfd;
    --card: #ffffff;
  }
  * { box-sizing: border-box; margin: 0; padding: 0; }
  html, body { width: 1178px; height: 1200px; overflow: hidden; }
  body {
    position: relative;
    font-family: "Roboto", sans-serif;
    background: linear-gradient(135deg, var(--bg-start) 0%, #9c9dcc 50%, var(--bg-end) 100%);
  }
  .brand {
    position: absolute; left: 48px; top: 76px;
    font-family: "Roboto", sans-serif; font-weight: 700; font-size: 56px;
    color: var(--navy-deep); letter-spacing: -0.5px;
  }
  .screen {
    position: absolute; left: 614px; top: 164px; width: 398px; height: 866px;
    background: var(--screen); border-radius: 36px; overflow: hidden;
    box-shadow: 0 24px 60px rgba(40, 40, 110, 0.25);
  }
  .progress { position: absolute; left: 22px; top: 80px; width: 297px; height: 12px;
    background: var(--track); border-radius: 6px; }
  .progress-fill { width: 188px; height: 100%; border-radius: 6px;
    background: repeating-linear-gradient(135deg, #3b3da0 0 3px, #5557b6 3px 6px);
    color: #fff; font-size: 8px; font-weight: 700; text-align: right; padding-right: 14px; line-height: 12px; }
  .progress-goal { position: absolute; left: 0; top: 96px; width: 319px; text-align: right;
    font-size: 8px; font-weight: 700; color: var(--navy); }
  .progress-goal::after { content: ""; display: inline-block; width: 2px; height: 10px;
    background: var(--navy); margin-left: 6px; vertical-align: middle; }
  .avatar { position: absolute; left: 334px; top: 66px; width: 38px; height: 38px; border-radius: 50%;
    background: radial-gradient(circle at 50% 45%, #8a6a55, #2e2a22); }
  .welcome { position: absolute; left: 21px; top: 128px; font-size: 32px; font-weight: 300;
    color: var(--navy); letter-spacing: -1px; white-space: nowrap; }
  .welcome strong { font-weight: 700; letter-spacing: -0.5px; }
  .section-label { position: absolute; left: 22px; font-size: 12.5px; font-weight: 500; color: var(--muted); }
  .see-all { position: absolute; right: 21px; font-size: 10px; color: #b5b5bd; }
  .challenge { position: absolute; left: 22px; top: 230px; width: 353px; height: 134px;
    background: var(--navy); color: #fff; padding: 16px 17px;
    box-shadow: 0 10px 22px rgba(43, 45, 143, 0.3); }
  .challenge h2 { font-size: 17px; font-weight: 700; margin-bottom: 10px; }
  .challenge p { font-size: 10.5px; font-weight: 300; line-height: 19px; width: 310px; }
  .challenge .stars { font-size: 11px; }
  .btn { position: absolute; right: 22px; bottom: 11px; border: 1px solid #fff; border-radius: 2px;
    padding: 5px 12px; font-size: 10.5px; font-weight: 700; }
  .stars { color: var(--orange); letter-spacing: 1px; font-size: 11px; }
  .stars .off { color: #f8d9b0; }
  .challenge .stars .off { color: #8b8dc6; }
  .row { position: absolute; left: 22px; display: flex; gap: 11px; }
  .reward { width: 122px; height: 134px; flex: none; background: var(--card); text-align: center;
    box-shadow: 0 6px 16px rgba(60, 60, 120, 0.08); padding-top: 12px; }
  .reward .amount { font-family: "Poppins", sans-serif; font-weight: 700; font-size: 33px; line-height: 34px;
    color: transparent; -webkit-text-stroke: 1.6px var(--orange); letter-spacing: 1px; }
  .reward .unit { font-size: 12.5px; font-weight: 500; color: var(--text); margin-top: 1px; }
  .reward .store { font-size: 12px; font-weight: 300; color: var(--text); margin: 16px 0 10px; white-space: nowrap; }
  .reward .store b { font-weight: 700; margin-right: 3px; }
</style>
</head>
<body>
  <div class="brand">Sparkle Pennant</div>

  <main class="screen">
    <div class="progress"><div class="progress-fill">2100 points</div></div>
    <div class="progress-goal">3000 points</div>
    <div class="avatar" role="img" aria-label="User profile photo"></div>

    <h1 class="welcome">Welcome back <strong>Dana</strong></h1>

    <div class="section-label" style="top:202px">Your new challenges</div>
    <section class="challenge">
      <h2>Weekly Pulse</h2>
      <p>Best marketing plan will chose by management, highest votes will be the winner.</p>
      <div class="stars">★★★★<span class="off">★</span></div>
      <div class="btn">Take Challenge</div>
    </section>

    <div class="section-label" style="top:423px">Received Rewards</div>
    <div class="see-all" style="top:425px">See All</div>
    <div class="row" style="top:452px">
      <div class="reward"><div class="amount">500</div><div class="unit">points</div>
        <div class="store"><b>$15</b> Fashion Store</div><div class="stars">★★★★★</div></div>
      <div class="reward"><div class="amount">250</div><div class="unit">points</div>
        <div class="store"><b>$10</b> Pagewise</div><div class="stars">★★★★<span class="off">★</span></div></div>
      <div class="reward"><div class="amount">100</div><div class="unit">points</div>
        <div class="store"><b>$5</b> Fashion Store</div><div class="stars">★★★<span class="off">★★</span></div></div>
    </div>

    <div class="section-label" style="top:634px">Ready to redeem</div>
    <div class="row" style="top:662px">
      <div class="reward"><div class="amount">1000</div><div class="unit">points</div>
        <div class="store"><b>$35</b> Fashion Store</div><div class="stars">★★★★★</div></div>
      <div class="reward"><div class="amount">250</div><div class="unit">points</div>
        <div class="store"><b>$15</b> Brightmart</div><div class="stars">★★★★<span class="off">★</span></div></div>
      <div class="reward"><div class="amount">100</div><div class="unit">points</div>
        <div class="store"><b>$15</b> Shopnest</div><div class="stars">★★★<span class="off">★★</span></div></div>
    </div>
  </main>
</body>
</html>
```